Gaming company needs web presence

PLEASE NOTE: We need just a simple web site. We are at least a year away from launching our first product, so the site only needs a small amount of information on it. The only people who will be visiting the web site are prospective employees, prospective investors who want a little information on the company, journalists who want a little more information, and people in the games industry who will visit to read blog posts about the development of our first game.

Brindle Hollow Studios is a new gaming company that wants to change how people think about video games. We are making games that we think can be so interesting to watch that people might want to tune into them instead of the TV.

The games we make are sophisticated, they are not for children, and we want to project an image of being serious about our craft and the brand we're trying to create. Our games are heavily focused on players interacting with each other in sophisticated ways: to negotiate, to compete, to fight, to come to each other's rescue, to cheer each other on, or to simply watch each other in awe.

We do not want a site that features lots of video game cliches like joysticks, 8 bit graphics, science fiction themes, or military themes. We are focused on craftsmanship, so we'd like to project a sense of precision, pride and deep purpose.

The purpose of this website is to create an image of our company that can help us recruit like-minded craftspeople and help find business partners. There will be no e-commerce, account creation, or forums for some time. The site should have:
-A front page that describes our business
-A section that describes our first game (we have only one for now)
-A section for employees to write blog posts. There should be something on the home page that shows links to the latest 3 blog posts.
-A section about founders that shows information about them.
-Contact information, lets people send us email

Our first game is one that looks very realistic. It takes place on a tropical island. We can't say a lot more about it in public yet, but I will say these things: it is not a game that children will play, it is not very violent, it would look more like a film than a typical video game.

And the site should be easily extendable when we have more content and more categories of content.

I've attached our official company logo with a color scheme we've been using, plus an alternate version of the logo. Please use this as a starting point for the web site's visual design. Also, I do not think it is necessary to use the dark background in the logo as the background throughout the site. I wouldn't rule it out, but I'd like to see some proposals with lighter backgrounds.

We need to be able to get code from you so that we can drop it on our server and get it running without extra effort. We need to be able to add content for Blog posts easily as well, so please indicate how that would work.
Updates

Hello everyone, Thanks for all of the great submissions so far. There are some important things I'd like to relay to everyone: We are at least a year away from launching our first game, so we only need a simple web site. Unfortunately, we can't share any screenshots or details about our first game yet. All of these submissions look great, but are far too complicated. Also, I really want to stress that we don't want to feature stock photography of people playing games, especially of children playing games. In fact, since we don't want to release any screenshots of our games and we don't have any good photography of ourselves working, it's best if there are no photographic images on the site for now.

Hello designers, Can you let me know if your designs include all the code that would let us drop the files on to our web server and easily get it up and running? Also, can you tell me how the blog posts would be created? Does your code run on a CMS? Thanks, Pellman

Hi Designers, we will be hosting this site with Wordpress, so we would prefer to have submissions ready to go on a Wordpress server. Thanks!

Target Market(s)

Investors, prospective employees, press, blog post readers.

Industry/Entity Type

Business

Font styles to use
Sans Serif

Requirements
Must have
• Simplicity first. Please use a color palette and fonts that match our logo.
Should not have
• Video game cliches. Flash animations or menus.
No children.
No photographs of people playing games.

(I realize this is very limiting, but we're keeping the sits as simple as possible for now)

```html
<!DOCTYPE html>
<html lang="en">
<head>
<meta charset="utf-8">
<title>Brindle Hollow Studios</title>
<link href="https://fonts.googleapis.com/css2?family=Montserrat:wght@400;600;700;800&family=Open+Sans:ital,wght@0,400;0,600;1,400&display=swap" rel="stylesheet">
<style>
:root{
  --bg-deep:#1f0b03;
  --bg-main:#2a1106;
  --bg-card:#4a1d08;
  --bg-footer:#180802;
  --orange:#d8843f;
  --orange-light:#e9964f;
  --orange-dark:#b3581f;
  --text-light:#f3e4d6;
  --text-muted:#c9a98f;
  --rule:#6a3a1c;
}
*{margin:0;padding:0;box-sizing:border-box}
html,body{width:1200px;height:2317px;overflow:hidden}
body{background:var(--bg-main);font-family:"Open Sans",sans-serif;color:var(--text-light);position:relative}
.abs{position:absolute}
h1,h2,h3,h4,.nav a,.logo{font-family:"Montserrat",sans-serif}

/* header */
.site-header{left:0;top:0;width:1200px;height:110px;background:var(--bg-main)}
.logo{left:0;width:1200px;top:0;height:110px;display:flex;align-items:center;justify-content:center;gap:14px;font-weight:700;font-size:30px;color:#fff;letter-spacing:2px;text-transform:uppercase}
.logo-dot{width:22px;height:22px;border-radius:50%;background:var(--orange)}

/* nav */
.nav{left:0;top:110px;width:1200px;height:64px;background:var(--orange);display:flex;padding-left:131px}
.nav a{display:block;height:64px;line-height:64px;padding:0 29px;color:#fff;font-weight:700;font-size:17px;text-decoration:none;letter-spacing:.5px}
.nav a.active{background:var(--bg-main);padding:0 27px}

/* hero */
.hero{left:0;top:174px;width:1200px;height:515px;background:linear-gradient(90deg,#f1ece6 0%,#e9ded2 35%,#c9a58b 55%,#9fb79d 80%,#7fae8d 100%)}
.hero-title{left:131px;top:340px;font-weight:800;font-size:52px;color:var(--orange);letter-spacing:-.5px}
.hero-sub{left:131px;top:418px;width:600px;font-family:"Open Sans",sans-serif;font-weight:600;font-size:35px;line-height:45px;color:#2a1608;letter-spacing:-1px}
.hero-arrow{top:401px;width:62px;height:62px;border-radius:50%;background:rgba(110,110,110,.55)}

/* content */
.content{left:0;top:689px;width:1200px;height:608px;background:var(--bg-main)}
.games-list{left:131px;top:727px;width:246px;height:334px;background:linear-gradient(180deg,var(--orange-light),var(--orange-dark));border:1px solid #f0a766;border-radius:3px}
.games-list h3{position:absolute;left:22px;top:14px;font-size:26px;font-weight:700;color:#3a1405}
.games-list h3 span{font-size:17px;color:#fff}
.games-list ul{position:absolute;left:20px;top:60px;width:204px;list-style:none}
.games-list li{height:39.5px;line-height:39.5px;border-bottom:1px dashed rgba(255,230,200,.5);font-size:11px;color:#fff;text-transform:uppercase}
.games-list li:last-child{border:none}
.search-box{left:131px;top:1079px;width:246px;height:142px;background:var(--bg-card);border-radius:3px}
.search-box h3{position:absolute;left:22px;top:13px;font-size:24px;color:var(--orange);font-weight:700}
.search-box p{position:absolute;left:22px;top:48px;width:210px;font-size:11.5px;line-height:19px;color:var(--text-muted)}
.search-input{position:absolute;left:22px;top:94px;width:175px;height:32px;border:1px solid #6b3a1d;font-size:11px;color:var(--text-muted);line-height:30px;padding-left:10px}
.search-go{position:absolute;left:200px;top:94px;width:34px;height:32px;background:var(--orange);border-radius:3px;font-family:"Montserrat",sans-serif;font-weight:700;font-size:15px;line-height:32px;text-align:center;color:#fff}

.section-title{font-weight:700;color:var(--orange);font-size:38px;border-bottom:1px solid var(--rule);width:665px;padding-bottom:6px}
.section-title span{font-size:22px;color:#f1ddc8;font-weight:700}
.welcome-title{left:403px;top:720px}
.welcome-text{left:403px;top:797px;width:660px;font-style:italic;font-size:12.5px;line-height:21px;color:var(--text-muted)}
.founders-title{left:403px;top:884px}
.founder{top:959px;width:207px;height:261px;background:var(--bg-card);border-radius:2px;text-align:center}
.founder-photo{position:absolute;left:20px;top:12px;width:166px;height:166px;border-radius:50%;border:3px solid #f2e3d3;background:linear-gradient(160deg,#8c7a64,#3d3a36)}
.founder-social{position:absolute;left:0;width:207px;top:160px;display:flex;justify-content:center;gap:8px}
.founder-social i{width:8px;height:8px;border-radius:50%;background:#fff;display:block}
.founder h4{position:absolute;left:0;width:207px;top:186px;font-size:12px;font-weight:700;color:#fff}
.founder p{position:absolute;left:12px;width:183px;top:208px;font-size:11.5px;line-height:19px;color:var(--text-muted)}

/* blog */
.blog{left:0;top:1297px;width:1200px;height:556px;background:var(--bg-deep)}
.blog-title{left:131px;top:1328px;width:938px;text-align:center;border-bottom:1px solid var(--rule);padding-bottom:6px;font-weight:700;font-size:38px;color:var(--orange)}
.blog-title span{font-size:22px;color:#f1ddc8}
.blog-arrow{top:1353px;width:38px;height:38px;border-radius:50%;background:var(--orange)}
.post{top:1427px;width:286px;height:381px;background:linear-gradient(180deg,#4c1e08 0%,#4c1e08 68%,#a4501d 100%)}
.post-image{position:absolute;left:0;top:0;width:286px;height:182px}
.post h4{position:absolute;left:15px;top:202px;font-size:18px;color:#fff;font-weight:700}
.post p{position:absolute;left:17px;top:237px;width:255px;font-size:11.5px;line-height:18.5px;color:#e3cdb9}
.post-meta{position:absolute;left:17px;top:340px;display:flex;align-items:center;gap:8px;font-family:"Montserrat",sans-serif;font-weight:700;font-size:18px;color:#fff}
.post-more{position:absolute;right:14px;top:343px;width:22px;height:22px;border-radius:50%;background:var(--orange)}

/* tweet */
.tweet-row{left:0;top:1853px;width:1200px;height:389px;background:var(--bg-main)}
.tweet-icon{left:131px;top:1898px;width:22px;height:22px;border-radius:50%;background:#fff}
.tweet-text{left:169px;top:1887px;width:580px;font-size:12.5px;line-height:21px;color:#eadbcc}
.tweet-text small{color:#8d6a52;font-size:11.5px}
.tweet-nav{top:1892px;width:30px;height:30px;border-radius:50%}

.contact-title{font-size:18px;font-weight:700;color:#fff}
.contact-info{left:131px;top:2008px}
.contact-text{left:131px;top:2050px;width:345px;font-size:11.5px;line-height:20px;color:#e2cfbd}
.contact-line{left:131px;display:flex;align-items:center;gap:10px;font-size:11.5px;color:#e2cfbd}
.form-title{left:514px;top:2008px}
.field{border:1px solid #6f3d1e;font-size:11px;color:#d8c3ae;padding:0 10px;line-height:34px}
.submit{left:884px;top:2106px;width:184px;height:36px;background:var(--orange);border-radius:2px;font-family:"Montserrat",sans-serif;font-weight:700;font-size:12.5px;line-height:36px;padding-left:10px;color:#fff}
.form-note{left:884px;top:2153px;width:184px;text-align:right;font-size:11.5px;color:#fff}

.site-footer{left:0;top:2242px;width:1200px;height:75px;background:var(--bg-footer)}
.copyright{left:131px;top:2268px;font-size:11.5px;color:#fff}
.footer-social{left:900px;top:2272px;display:flex;gap:12px}
.footer-social i{display:block;width:11px;height:11px;border-radius:50%;background:var(--orange)}
</style>
</head>
<body>

<header class="abs site-header">
  <div class="abs logo"><span class="logo-dot"></span>Brindle Hollow Studios</div>
</header>

<nav class="abs nav">
  <a class="active">HOME</a><a>ABOUT US</a><a>BLOG</a><a>FOUNDERS</a><a>OUR GAMES</a><a>NEWS</a><a>CONTACT US</a>
</nav>

<section class="abs hero" role="img" aria-label="Hero banner photograph in warm cream and soft green tones"></section>
<h1 class="abs hero-title">BRINDLE HOLLOW STUDIOS</h1>
<p class="abs hero-sub">Neque porro quisquam est qui dolore m ipsum Neque porro quisq....</p>
<svg class="abs hero-arrow" style="left:15px" viewBox="0 0 62 62"><path d="M35 21 L25 31 L35 41" fill="none" stroke="#fff" stroke-width="2.5"/></svg>
<svg class="abs hero-arrow" style="left:1116px" viewBox="0 0 62 62"><path d="M27 21 L37 31 L27 41" fill="none" stroke="#fff" stroke-width="2.5"/></svg>

<div class="abs content"></div>

<aside class="abs games-list">
  <h3>LIST <span>OUR GAMES</span></h3>
  <ul>
    <li>Sed ut perspiciatis unde omnis</li>
    <li>Iste natus error sit voluptatem</li>
    <li>Accusantium doloremque</li>
    <li>Dantium, totam rem aperia lore</li>
    <li>Eaque ipsa quae ab illo inve</li>
    <li>Tore veritatis et qu</li>
    <li>Asi arhitecto</li>
  </ul>
</aside>

<aside class="abs search-box">
  <h3>SEARCH</h3>
  <p>Sed ut perspiciatis unde omnis iste tus error sit voluptatem</p>
  <div class="search-input">Keyword...</div>
  <div class="search-go">GO</div>
</aside>

<h2 class="abs section-title welcome-title">WELCOME <span>TO BRINDLE HOLLOW STUDIOS</span></h2>
<p class="abs welcome-text">Sed ut perspiciatis unde omnis iste natus error sit voluptatem accusantium doloremque laudantium, totam rem aperiam, eaque ipsa quae ab illo inventore veritatis et quasi architecto beatae vitae dicta sunt explicabo. Nemo enim ipsam voluptatem quia voluptas sit aspernatur</p>

<h2 class="abs section-title founders-title">ABOUT <span>OUR FOUNDERS</span></h2>

<article class="abs founder" style="left:403px">
  <div class="founder-photo" role="img" aria-label="Founder portrait"></div>
  <div class="founder-social"><i></i><i></i></div>
  <h4>SED UT PERSPICIATIS</h4>
  <p>Sed ut perspiciatis unde omnis iste natus error sit voluptatem</p>
</article>
<article class="abs founder" style="left:633px">
  <div class="founder-photo" role="img" aria-label="Founder portrait"></div>
  <div class="founder-social"><i></i><i></i></div>
  <h4>SED UT PERSPICIATIS</h4>
  <p>Sed ut perspiciatis unde omnis iste natus error sit voluptatem</p>
</article>
<article class="abs founder" style="left:862px">
  <div class="founder-photo" role="img" aria-label="Founder portrait"></div>
  <div class="founder-social"><i></i><i></i></div>
  <h4>SED UT PERSPICIATIS</h4>
  <p>Sed ut perspiciatis unde omnis iste natus error sit voluptatem</p>
</article>

<section class="abs blog"></section>
<h2 class="abs blog-title">LATEST <span>BLOG POSTS</span></h2>
<svg class="abs blog-arrow" style="left:131px" viewBox="0 0 38 38"><circle cx="19" cy="19" r="19" fill="#d8843f"/><path d="M22 12 L15 19 L22 26" fill="none" stroke="#fff" stroke-width="3"/></svg>
<svg class="abs blog-arrow" style="left:1030px" viewBox="0 0 38 38"><circle cx="19" cy="19" r="19" fill="#d8843f"/><path d="M16 12 L23 19 L16 26" fill="none" stroke="#fff" stroke-width="3"/></svg>

<article class="abs post" style="left:131px">
  <div class="post-image" role="img" aria-label="Blog post image: racing game scene" style="background:linear-gradient(180deg,#6b94c4,#6f8a4a 60%,#2c2c2c)"></div>
  <h4>SED UT PERSPICIATIS</h4>
  <p>Sed ut perspiciatis unde omnis iste natus error sit voluptatem tium doloremque laudantium,Sed ut perspiciatis unde omnis iste natus error sit voluptatem</p>
  <div class="post-meta"><svg width="26" height="26" viewBox="0 0 26 26"><path d="M3 23 L5 16 L18 3 L23 8 L10 21 Z" fill="#2a1106"/></svg>04-AUG 2014</div>
  <span class="post-more"></span>
</article>
<article class="abs post" style="left:457px">
  <div class="post-image" role="img" aria-label="Blog post image: fantasy game artwork" style="background:linear-gradient(150deg,#2e6f8a,#6a4a3a 55%,#2b3f6a)"></div>
  <h4>SED UT PERSPICIATIS</h4>
  <p>Sed ut perspiciatis unde omnis iste natus error sit voluptatem tium doloremque laudantium,Sed ut perspiciatis unde omnis iste natus error sit voluptatem</p>
  <div class="post-meta"><svg width="26" height="26" viewBox="0 0 26 26"><path d="M3 23 L5 16 L18 3 L23 8 L10 21 Z" fill="#2a1106"/></svg>04-AUG 2014</div>
  <span class="post-more"></span>
</article>
<article class="abs post" style="left:783px">
  <div class="post-image" role="img" aria-label="Blog post image: strategy game arena" style="background:radial-gradient(circle at 45% 55%,#8a9a4a,#4e5a2a 60%,#3a3a22)"></div>
  <h4>SED UT PERSPICIATIS</h4>
  <p>Sed ut perspiciatis unde omnis iste natus error sit voluptatem tium doloremque laudantium,Sed ut perspiciatis unde omnis iste natus error sit voluptatem</p>
  <div class="post-meta"><svg width="26" height="26" viewBox="0 0 26 26"><path d="M3 23 L5 16 L18 3 L23 8 L10 21 Z" fill="#2a1106"/></svg>04-AUG 2014</div>
  <span class="post-more"></span>
</article>

<section class="abs tweet-row"></section>
<span class="abs tweet-icon"></span>
<p class="abs tweet-text">RT @mervane: Trade growth ideas with other founders. Look for ways to cross promote. Small startups today may be big friends later. (9/10) <small>2 days ago</small></p>
<svg class="abs tweet-nav" style="left:1002px" viewBox="0 0 30 30"><circle cx="15" cy="15" r="15" fill="#4a1a06"/><path d="M17 9 L11 15 L17 21" fill="none" stroke="#2a1106" stroke-width="3"/></svg>
<svg class="abs tweet-nav" style="left:1038px" viewBox="0 0 30 30"><circle cx="15" cy="15" r="15" fill="#d8843f"/><path d="M13 9 L19 15 L13 21" fill="none" stroke="#2a1106" stroke-width="3"/></svg>

<h3 class="abs contact-title contact-info">CONTACT INFO</h3>
<p class="abs contact-text">Ut volutpat consectetur aliquam. Curabitur auctor in nis ulum ornare. Sed consequat, augue condimentum fermentum gravida, metus elit vehicula dui.</p>
<div class="abs contact-line" style="top:2131px"><svg width="8" height="12" viewBox="0 0 8 12"><rect x="1" y="0.5" width="6" height="11" rx="1" fill="none" stroke="#fff"/></svg>+1 555 0142 889</div>
<div class="abs contact-line" style="top:2151px"><svg width="10" height="8" viewBox="0 0 10 8"><rect width="10" height="8" fill="#fff"/><path d="M0 0 L5 4 L10 0" fill="none" stroke="#2a1106"/></svg>hello@brindlehollow.net</div>

<h3 class="abs contact-title form-title">QUICK CONTACT FORM</h3>
<div class="abs field" style="left:514px;top:2056px;width:171px;height:36px">your name</div>
<div class="abs field" style="left:698px;top:2056px;width:172px;height:36px">email address</div>
<div class="abs field" style="left:884px;top:2056px;width:184px;height:36px">subject</div>
<div class="abs field" style="left:514px;top:2106px;width:356px;height:104px">your name</div>
<div class="abs submit">SUBMIT YOUR MESSAGE ›</div>
<p class="abs form-note">Make sure you put a valid email.</p>

<footer class="abs site-footer"></footer>
<p class="abs copyright">© 2014. All rights reserved.</p>
<div class="abs footer-social"><i></i><i></i><i></i><i></i><i></i><i></i><i></i></div>

</body>
</html>
```